Organic Vegan Crispread - 100% Free of Soja

We are looking to update our labels for our current range of Crispbreads. They are all produced in Denmark, they are organic, vegan og we do not use any soy at all.

The crisp breads are high products and aimed for the gourmet market retail.

The range contains 6 different at the moment and will have 4 new types coming soon. The current six products are following:
Organic Crispbread Salt
Organic Crispbread Herbs
Organic Crispbread spices
Organic Crispbread Seaweed
Organic Crispbread Glutenfree
Organic Cripsbread Protein (Green Proteins)

The range will have to contain our logo and our name.

Measurements of Labels:
60mm wide
50mm High

Only front label design.

Target Market(s)

High End Consumers

Requirements
Must have
• Company Logo
Organic logo red (under this we need to write "QX-VAL-738")
Organic logo Green (under this we need to write "EU / ikke EU-jordbrug")
Name
Visuel identity per type
Nice to have
• Red line throughout the range
Should not have
• No Bling Bling

```html
<!DOCTYPE html>
<html lang="en">
<head>
<meta charset="utf-8">
<title>Vester Organic Foods – Crispbread Labels</title>
<link rel="stylesheet" href="https://fonts.googleapis.com/css2?family=Allura&family=Anton&family=Josefin+Sans:wght@600&display=swap">
<style>
  :root {
    --brand-red: #b30005;
    --edge-light: #f6d3c8;
    --terrazzo: #f3c3b0;
    --gold: #c49a5c;
    --white: #ffffff;
    --badge-green: #8cc63f;
    --badge-red: #d9101a;
    --ink: #333333;
  }
  * { margin: 0; padding: 0; box-sizing: border-box; }
  html, body { width: 946px; height: 1200px; overflow: hidden; background: var(--white); }
  .sheet {
    position: relative;
    width: 946px; height: 1200px;
    display: grid;
    grid-template-columns: 426px 426px;
    grid-auto-rows: 356px;
    column-gap: 28px;
    row-gap: 30px;
    padding: 36px 0 0 33px;
  }
  .label { display: block; width: 426px; height: 356px; }

  .label--glutenfree { --band: #f07a84; --box: #e04a58; --title: #8a2a30; --variant: #8a2a30; }
  .label--protein    { --band: #cf913c; --box: #6e4e33; --title: #5a3e26; --variant: #c99440; }
  .label--spices     { --band: #6b1012; --box: #4a0808; --title: #f07a1a; --variant: #f08a1a; }
  .label--seaweed    { --band: #45acd0; --box: #0d4a68; --title: #1b4a66; --variant: #2a7fa6; }
  .label--salt       { --band: #5fb6ae; --box: #2a6e68; --title: #1f5854; --variant: #4a9f97; }
  .label--herb       { --band: #62cf78; --box: #1e9138; --title: #1e6e34; --variant: #0f6d26; }

  .sky { fill: var(--brand-red); }
  .edge { fill: var(--edge-light); }
  .band { fill: var(--band); }
  .box { fill: var(--box); }
  .stripe { stroke: var(--box); stroke-width: 5; opacity: .75; }
  .terrazzo { fill: var(--terrazzo); }
  .rule { fill: var(--brand-red); }

  .seal { fill: var(--white); stroke: var(--gold); stroke-width: 4; }
  .seal-name { fill: var(--gold); font-family: "Josefin Sans", sans-serif; font-weight: 600; text-anchor: middle; }

  .script { fill: var(--white); font-family: "Allura", cursive; font-size: 70px; }
  .title { fill: var(--title); font-family: "Anton", sans-serif; font-size: 64px; }
  .variant { fill: var(--variant); font-family: "Anton", sans-serif; font-size: 40px; text-anchor: middle; }
  .variant-sub { fill: var(--variant); font-family: "Josefin Sans", sans-serif; font-weight: 600; font-size: 10px; text-anchor: middle; }

  .cert-green { fill: var(--badge-green); }
  .cert-card { fill: var(--white); }
  .cert-dot { fill: var(--badge-red); }
  .cert-caption { fill: var(--ink); font-family: "Josefin Sans", sans-serif; font-weight: 600; font-size: 8.5px; }
</style>
</head>
<body>
<main class="sheet">

  <!-- Glutenfree -->
  <svg class="label label--glutenfree" viewBox="0 0 550 460" role="group" aria-label="Organic Crispbread Glutenfree label">
    <rect class="sky" width="550" height="460"/>
    <polygon class="edge" points="0,266 550,86 550,95 0,275"/>
    <polygon class="band" points="0,275 550,95 550,275 0,455"/>
    <polygon class="box" points="450,128 550,95 550,275 450,308"/>
    <line class="stripe" x1="0" y1="438" x2="340" y2="327"/>
    <line class="stripe" x1="250" y1="220" x2="450" y2="155"/>
    <polygon class="terrazzo" points="0,455 550,275 550,446 0,446" role="img" aria-label="Speckled terrazzo texture in soft pink tones"/>
    <rect class="rule" y="446" width="550" height="14"/>
    <circle class="seal" cx="150" cy="148" r="86"/>
    <text class="seal-name" x="150" y="146" font-size="24">VESTER</text>
    <text class="seal-name" x="150" y="168" font-size="11">ORGANIC FOODS</text>
    <text class="script" transform="translate(82,338) rotate(-18)">Organic</text>
    <text class="title" textLength="350" transform="translate(112,398) rotate(-18) skewX(-10)">CRISPBREAD</text>
    <text class="variant" font-size="34" textLength="170" transform="translate(514,205) rotate(-90)">GLUTENFREE</text>
    <rect class="cert-green" x="348" y="366" width="75" height="40"/>
    <rect class="cert-card" x="436" y="366" width="86" height="40"/>
    <circle class="cert-dot" cx="456" cy="386" r="15"/>
    <text class="cert-caption" x="346" y="418">EU / ikke EU-jordbrug</text>
    <text class="cert-caption" x="452" y="418">QX-VAL-738</text>
  </svg>

  <!-- Protein -->
  <svg class="label label--protein" viewBox="0 0 550 460" role="group" aria-label="Organic Crispbread Protein label">
    <rect class="sky" width="550" height="460"/>
    <polygon class="edge" points="0,266 550,86 550,95 0,275"/>
    <polygon class="band" points="0,275 550,95 550,275 0,455"/>
    <polygon class="box" points="450,128 550,95 550,275 450,308"/>
    <line class="stripe" x1="0" y1="438" x2="340" y2="327"/>
    <line class="stripe" x1="250" y1="220" x2="450" y2="155"/>
    <polygon class="terrazzo" points="0,455 550,275 550,446 0,446" role="img" aria-label="Speckled terrazzo texture in soft pink tones"/>
    <rect class="rule" y="446" width="550" height="14"/>
    <circle class="seal" cx="150" cy="148" r="86"/>
    <text class="seal-name" x="150" y="146" font-size="24">VESTER</text>
    <text class="seal-name" x="150" y="168" font-size="11">ORGANIC FOODS</text>
    <text class="script" transform="translate(82,338) rotate(-18)">Organic</text>
    <text class="title" textLength="350" transform="translate(112,398) rotate(-18) skewX(-10)">CRISPBREAD</text>
    <text class="variant" transform="translate(506,210) rotate(-90)">PROTEIN</text>
    <text class="variant-sub" transform="translate(527,210) rotate(-90)">GREEN PROTEINS</text>
    <rect class="cert-green" x="348" y="366" width="75" height="40"/>
    <rect class="cert-card" x="436" y="366" width="86" height="40"/>
    <circle class="cert-dot" cx="456" cy="386" r="15"/>
    <text class="cert-caption" x="346" y="418">EU / ikke EU-jordbrug</text>
    <text class="cert-caption" x="452" y="418">QX-VAL-738</text>
  </svg>

  <!-- Spices -->
  <svg class="label label--spices" viewBox="0 0 550 460" role="group" aria-label="Organic Crispbread Spices label">
    <rect class="sky" width="550" height="460"/>
    <polygon class="edge" points="0,266 550,86 550,95 0,275"/>
    <polygon class="band" points="0,275 550,95 550,275 0,455"/>
    <polygon class="box" points="450,128 550,95 550,275 450,308"/>
    <line class="stripe" x1="0" y1="438" x2="340" y2="327"/>
    <line class="stripe" x1="250" y1="220" x2="450" y2="155"/>
    <polygon class="terrazzo" points="0,455 550,275 550,446 0,446" role="img" aria-label="Speckled terrazzo texture in soft pink tones"/>
    <rect class="rule" y="446" width="550" height="14"/>
    <circle class="seal" cx="150" cy="148" r="86"/>
    <text class="seal-name" x="150" y="146" font-size="24">VESTER</text>
    <text class="seal-name" x="150" y="168" font-size="11">ORGANIC FOODS</text>
    <text class="script" transform="translate(82,338) rotate(-18)">Organic</text>
    <text class="title" textLength="350" transform="translate(112,398) rotate(-18) skewX(-10)">CRISPBREAD</text>
    <text class="variant" transform="translate(514,205) rotate(-90)">SPICES</text>
    <rect class="cert-green" x="348" y="366" width="75" height="40"/>
    <rect class="cert-card" x="436" y="366" width="86" height="40"/>
    <circle class="cert-dot" cx="456" cy="386" r="15"/>
    <text class="cert-caption" x="346" y="418">EU / ikke EU-jordbrug</text>
    <text class="cert-caption" x="452" y="418">QX-VAL-738</text>
  </svg>

  <!-- Seaweed -->
  <svg class="label label--seaweed" viewBox="0 0 550 460" role="group" aria-label="Organic Crispbread Seaweed label">
    <rect class="sky" width="550" height="460"/>
    <polygon class="edge" points="0,266 550,86 550,95 0,275"/>
    <polygon class="band" points="0,275 550,95 550,275 0,455"/>
    <polygon class="box" points="450,128 550,95 550,275 450,308"/>
    <line class="stripe" x1="0" y1="438" x2="340" y2="327"/>
    <line class="stripe" x1="250" y1="220" x2="450" y2="155"/>
    <polygon class="terrazzo" points="0,455 550,275 550,446 0,446" role="img" aria-label="Speckled terrazzo texture in soft pink tones"/>
    <rect class="rule" y="446" width="550" height="14"/>
    <circle class="seal" cx="150" cy="148" r="86"/>
    <text class="seal-name" x="150" y="146" font-size="24">VESTER</text>
    <text class="seal-name" x="150" y="168" font-size="11">ORGANIC FOODS</text>
    <text class="script" transform="translate(82,338) rotate(-18)">Organic</text>
    <text class="title" textLength="350" transform="translate(112,398) rotate(-18) skewX(-10)">CRISPBREAD</text>
    <text class="variant" transform="translate(514,205) rotate(-90)">SEAWEED</text>
    <rect class="cert-green" x="348" y="366" width="75" height="40"/>
    <rect class="cert-card" x="436" y="366" width="86" height="40"/>
    <circle class="cert-dot" cx="456" cy="386" r="15"/>
    <text class="cert-caption" x="346" y="418">EU / ikke EU-jordbrug</text>
    <text class="cert-caption" x="452" y="418">QX-VAL-738</text>
  </svg>

  <!-- Salt -->
  <svg class="label label--salt" viewBox="0 0 550 460" role="group" aria-label="Organic Crispbread Salt label">
    <rect class="sky" width="550" height="460"/>
    <polygon class="edge" points="0,266 550,86 550,95 0,275"/>
    <polygon class="band" points="0,275 550,95 550,275 0,455"/>
    <polygon class="box" points="450,128 550,95 550,275 450,308"/>
    <line class="stripe" x1="0" y1="438" x2="340" y2="327"/>
    <line class="stripe" x1="250" y1="220" x2="450" y2="155"/>
    <polygon class="terrazzo" points="0,455 550,275 550,446 0,446" role="img" aria-label="Speckled terrazzo texture in soft pink tones"/>
    <rect class="rule" y="446" width="550" height="14"/>
    <circle class="seal" cx="150" cy="148" r="86"/>
    <text class="seal-name" x="150" y="146" font-size="24">VESTER</text>
    <text class="seal-name" x="150" y="168" font-size="11">ORGANIC FOODS</text>
    <text class="script" transform="translate(82,338) rotate(-18)">Organic</text>
    <text class="title" textLength="350" transform="translate(112,398) rotate(-18) skewX(-10)">CRISPBREAD</text>
    <text class="variant" transform="translate(514,205) rotate(-90)">SALT</text>
    <rect class="cert-green" x="348" y="366" width="75" height="40"/>
    <rect class="cert-card" x="436" y="366" width="86" height="40"/>
    <circle class="cert-dot" cx="456" cy="386" r="15"/>
    <text class="cert-caption" x="346" y="418">EU / ikke EU-jordbrug</text>
    <text class="cert-caption" x="452" y="418">QX-VAL-738</text>
  </svg>

  <!-- Herb -->
  <svg class="label label--herb" viewBox="0 0 550 460" role="group" aria-label="Organic Crispbread Herb label">
    <rect class="sky" width="550" height="460"/>
    <polygon class="edge" points="0,266 550,86 550,95 0,275"/>
    <polygon class="band" points="0,275 550,95 550,275 0,455"/>
    <polygon class="box" points="450,128 550,95 550,275 450,308"/>
    <line class="stripe" x1="0" y1="438" x2="340" y2="327"/>
    <line class="stripe" x1="250" y1="220" x2="450" y2="155"/>
    <polygon class="terrazzo" points="0,455 550,275 550,446 0,446" role="img" aria-label="Speckled terrazzo texture in soft pink tones"/>
    <rect class="rule" y="446" width="550" height="14"/>
    <circle class="seal" cx="150" cy="148" r="86"/>
    <text class="seal-name" x="150" y="146" font-size="24">VESTER</text>
    <text class="seal-name" x="150" y="168" font-size="11">ORGANIC FOODS</text>
    <text class="script" transform="translate(82,338) rotate(-18)">Organic</text>
    <text class="title" textLength="350" transform="translate(112,398) rotate(-18) skewX(-10)">CRISPBREAD</text>
    <text class="variant" transform="translate(514,205) rotate(-90)">HERB</text>
    <rect class="cert-green" x="348" y="366" width="75" height="40"/>
    <rect class="cert-card" x="436" y="366" width="86" height="40"/>
    <circle class="cert-dot" cx="456" cy="386" r="15"/>
    <text class="cert-caption" x="346" y="418">EU / ikke EU-jordbrug</text>
    <text class="cert-caption" x="452" y="418">QX-VAL-738</text>
  </svg>

</main>
</body>
</html>
```